Start Up sucht Sticker-, Postkarten- und Herz-Design für Gastgeschenk Seedballs für Hochzeiten
Zielgruppe
Hallo! Wir sind ein Start Up aus dem Saatgutbereich mit verschiedenen Marken. Für unser neues Produkt:
Seedballs in 50er und 100er Abpackungen für Hochzeiten (Gastgeschenke) suchen wir 3 Designs: Zum einen ein Design für den herzförmigen Anhänger (die an die Seedballs in kleinen Organzasäckchen gehangen werden), eine Postkarte die den zu Trauenden einen wunderschönen Tag wünscht und den Sticker der außen auf die Kraftkartonverpackung geklebt wird. Falls die Produkte gut angenommen werden, werden wir eine komplette Faltkartonverpackung erstellen und einsetzen.
Aufgabenstellung
Wir haben für die Marke 'Wiesenfunke' bereits ein Logo und einige Verpackungen designt. Siehe Anhang. Aber es soll hier vor allem um den Zweck der Gastgeschenke gehen mit Hauptdesign 'Hochzeit'. Logo, Organzasäckchen, Vorlage Herz anbei.
Es solls ich vor allem um das Thema 'Hochzeit' drehen, weniger um die Marke an sich. Das genutzte Papier soll weiß sein, da dies mit den meisten Hochzeitsvorlagen und Dekos zusammen passt.
Als vielleicht passende Fonts kommen: Brittany, Monterchi Serif oder andere in Frage.
Enthalten sind bei den beiden Sets
50er:
50 Seedballs in Kraftpapiertüte mit Sticker
50 Organzasäckchen
50 herzförmige Geschenkanhänger
1x Postkarte für das Ehepaar
100er
100 Seedballs in Kraftpapiertüte mit Sticker
100 Organzasäckchen
100 herzförmige Geschenkanhänger
Folgende Formate sollen genutzt werden:
Postkarte: DIN A6
Herzförmiger Geschenkanhänger: 5x5cm
Sticker für die Verpackung:
50x Seedballs: 8x18cm
100x Seedballs: 10x20cm
Ideen:
Postkarte:
Es soll nur eine allgemeine Postkarte sein die den Trauenden einen wunderschönen Tag und eine wunderschöne Ehe wünscht. Die Rückseite kann ebenfalls designed werden.
Herzförmiger Geschenkanhänger für die Organzasäckchen mit Seedball:
Dort soll etwas wie 'Lasst unsere Liebe wachsen' oder ähnliches stehen, allgemein gehalten. Die Rückseite soll eine ganz kleine Anleitung wie die Seedballs funktionieren enthalten. Siehe Design was es schon gibt.
Das Design soll sich vor allem um Hochzeit und das Thema Gastgeschenk drehen. Außen soll die Anzahl der befindlichen Seedballs stehen (50 bzw. 100) + EAN Code + unsere Kontaktdaten. EAN Codes und Daten werden von uns gestellt. Nutzt bitte zu erst einfache Platzhalter.
Wenn weitere Infos benötigt werden, dann gerne melden. Wir freuen uns auf eure Vorschläge.

```html
<!DOCTYPE html>
<html lang="de">
<head>
<meta charset="utf-8">
<title>Wiesenfunke – Hochzeitskarte</title>
<link rel="stylesheet" href="https://fonts.googleapis.com/css2?family=Cookie&display=swap">
<style>
  :root {
    --kraft: #e9dfcc;
    --kraft-shade: #e2d6bf;
    --ink: #3a2a27;
  }
  html, body {
    margin: 0;
    padding: 0;
    width: 1200px;
    height: 865px;
    overflow: hidden;
    background: var(--kraft);
  }
  .postcard {
    position: relative;
    width: 1200px;
    height: 865px;
    background: radial-gradient(ellipse at 50% 45%, var(--kraft) 0%, var(--kraft-shade) 100%);
    color: var(--ink);
    font-family: "Cookie", cursive;
    text-align: center;
  }
  .brand {
    position: absolute;
    top: 24px;
    left: 0;
    width: 100%;
  }
  .brand-mark {
    display: block;
    margin: 0 auto;
  }
  .brand-name {
    margin: 2px 0 0;
    font-size: 76px;
    font-weight: 400;
    line-height: 1;
    color: var(--ink);
  }
  .greeting {
    position: absolute;
    top: 318px;
    left: 0;
    width: 100%;
    margin: 0;
    font-size: 66px;
    line-height: 81.5px;
    color: var(--ink);
  }
</style>
</head>
<body>
  <main class="postcard">
    <header class="brand">
      <svg class="brand-mark" width="190" height="190" viewBox="0 0 190 190" aria-hidden="true">
        <circle cx="95" cy="95" r="89" fill="none" stroke="var(--ink)" stroke-width="4"/>
      </svg>
      <h1 class="brand-name">Wiesenfunke</h1>
    </header>
    <p class="greeting">
      Wir freuen uns sehr,<br>
      euch als frisch vermähltes Paar<br>
      beglückwünschen zu dürfen.<br>
      Mögen alle eure Träume und Wünsche<br>
      in Erfüllung gehen und eure<br>
      Liebe für immer anhalten.
    </p>
  </main>
</body>
</html>
```